Digital marketing agency needs a new website design

We need a new responsive design for our website: https://brivolta.com/

Brivolta is a french digital marketing company who specializes in helping companies rank higher on Quendo search engine for their keywords in order to be more visible and have more traffic and clients.

I need you to design these 5 pages:
- Home page: https://brivolta.com
- Pricing page: https://brivolta.com/packs-backlinks/
- Contact page: https://brivolta.com/contact/
- Thank you page: https://brivolta.com/merci-temp/
- Simple page : https://brivolta.com/a-propos/

Here is a list of websites that we like their design. Use it for inspiration, but make sure it is different :

https://fenrolt.io/ (this is the one I like the most)
https://ubro.com/
http://www.garvelnest.com/
https://lumbardeau.fr/
https://www.tressaplank.com/home
https://dovermick.com/fr/
https://kalvoxa.io/
https://tramoisenet.fr/

I want a 75% color background and 25% white. You should use many bright/pastel colors like this website : https://fenrolt.io/

Keep the contact form in the website header.

Target Market(s)

small business owners

Industry/Entity Type

Digital Marketing

Number of Pages Required

5+ page

Font styles to use
Sans Serif

Colors

Designer to choose colors to be used in the design.

Requirements
Must have
• Contact form in header.
• Prominent call-to-action buttons.
• Use of at least 1 flashy color, possible to use many.
• Keep the 3 chart images.
• Keep client testimonials

```html
<!DOCTYPE html>
<html lang="en">
<head>
<meta charset="utf-8">
<title>Brivolta – French Backlinks on Quality Magazines and Blogs</title>
<link rel="stylesheet" href="https://fonts.googleapis.com/css2?family=Montserrat:wght@400;500;600;700&family=Open+Sans:wght@400;600;700&display=swap">
<style>
:root{
  --blue:#1e7fe0;
  --blue-light:#4ab0f5;
  --blue-dark:#1566c4;
  --navy:#1c2b3a;
  --text:#5d6873;
  --muted:#8b96a1;
  --bg-soft:#f6f8fb;
  --bg-grey:#f3f3f4;
  --white:#ffffff;
  --pink:#ef4a7a;
  --step-blue:#2f8fe8;
  --teal:#23c2cb;
  --purple:#5a52c8;
  --yellow:#f5c518;
  --line:#e5e9ee;
  --chart-line:#1a73d8;
  --chart-fill:#e3f0fb;
  --pointer:#7db6ea;
}
*{box-sizing:border-box;margin:0;padding:0}
html,body{width:1200px;height:4138px;overflow:hidden}
body{font-family:"Open Sans",Arial,sans-serif;color:var(--text);background:var(--white);position:relative}
h1,h2,h3,h4,.brand,.btn,.nav a{font-family:"Montserrat",Arial,sans-serif}
.abs{position:absolute}
.brand{font-weight:700;font-size:26px;letter-spacing:1px;display:flex;align-items:center;gap:8px}
.brand i{width:10px;height:10px;background:var(--yellow);display:block}
.btn{display:inline-flex;align-items:center;justify-content:center;gap:10px;background:var(--blue);color:#fff;font-size:12px;font-weight:600;letter-spacing:1px;text-transform:uppercase;text-decoration:none;border-radius:3px;box-shadow:0 6px 14px rgba(30,127,224,.3)}
.label{font-family:"Montserrat",Arial,sans-serif;color:var(--blue);font-size:13px;font-weight:700;letter-spacing:1px;text-transform:uppercase}
.section-title{font-size:22px;font-weight:700;color:var(--navy)}

/* Hero */
.hero{position:absolute;left:0;top:0;width:1200px;height:720px;background:linear-gradient(180deg,#1a78dc 0%,#3a9ff0 70%,#5ab8f7 100%);overflow:hidden}
.hero-wave{position:absolute;left:0;top:0;width:1200px;height:720px}
.nav{position:absolute;top:20px;left:0;width:1200px;height:40px}
.nav .brand{position:absolute;left:157px;top:4px;color:#fff}
.nav a{position:absolute;top:10px;color:#fff;font-size:13px;text-decoration:none;font-weight:500}
.hero h1{position:absolute;top:92px;left:0;width:1200px;text-align:center;color:#fff;font-size:36px;line-height:44px;font-weight:700}
.hero .sub{position:absolute;top:184px;left:0;width:1200px;text-align:center;color:#fff;font-size:14px;line-height:19px}
.hero .sub b{color:var(--yellow);font-weight:600}
.form-card{position:absolute;left:237px;top:265px;width:723px;height:383px;background:#fff;border-radius:4px;box-shadow:0 14px 40px rgba(20,60,120,.18);padding:38px 66px 0}
.form-card h2{text-align:center;font-size:19px;color:var(--navy);font-weight:700}
.form-card .hint{text-align:center;font-size:11px;color:var(--muted);margin-top:6px}
.form-card .rule{width:36px;height:2px;background:var(--yellow);margin:8px auto 14px}
.field{border:1px solid #bfe0fb;border-radius:3px;height:40px;font-size:11px;color:var(--muted);padding:12px 14px;background:#fff}
.row{display:flex;gap:14px;margin-bottom:10px}
.row .field{flex:1}
.field.wide{margin-bottom:10px}
.field.area{height:76px}
.form-card .btn{display:flex;width:240px;height:42px;margin:10px auto 0}

/* Logos */
.logos{position:absolute;top:700px;left:160px;width:880px;height:60px;display:flex;justify-content:space-between;align-items:center}
.logos span{font-family:"Montserrat",Arial,sans-serif;font-size:22px;font-weight:600;color:#6b737b}

/* About */
.about{position:absolute;left:0;top:800px;width:1200px;height:400px;background:var(--bg-soft);border-top:1px solid var(--line);text-align:center}
.about .label{position:absolute;top:80px;left:0;width:1200px}
.about h2{position:absolute;top:114px;left:0;width:1200px;font-size:20px}
.about p{position:absolute;top:166px;left:240px;width:720px;font-size:12px;line-height:20px;color:var(--text)}
.about .btn{position:absolute;left:500px;top:276px;width:198px;height:44px}

/* Steps */
.steps{position:absolute;left:0;top:1200px;width:1200px;height:607px;background:var(--bg-grey)}
.step{position:absolute;width:157px;height:197px;border-radius:4px;color:#fff;text-align:center;box-shadow:0 10px 22px rgba(0,0,0,.12)}
.step .tag{position:absolute;top:-14px;left:32px;width:93px;height:28px;border-radius:14px;background:#fff;font-size:12px;line-height:28px;font-family:"Montserrat",Arial,sans-serif;font-weight:500}
.step svg{display:block;margin:44px auto 10px}
.step h3{font-size:15px;line-height:19px;font-weight:700;padding:0 14px}
.s1{left:160px;top:202px;background:var(--pink)}.s1 .tag{color:var(--pink)}
.s2{left:342px;top:91px;background:var(--step-blue)}.s2 .tag{color:var(--step-blue)}
.s3{left:527px;top:202px;background:var(--purple)}.s3 .tag{color:var(--purple)}
.s4{left:342px;top:326px;background:var(--teal)}.s4 .tag{color:var(--teal)}
.steps-copy{position:absolute;left:728px;top:202px;width:320px}
.steps-copy h2{font-size:19px;line-height:26px;color:var(--navy);font-weight:700;margin-top:16px}
.steps-copy p{font-size:11px;line-height:17px;margin-top:12px;color:var(--text)}
.steps-copy .btn{width:172px;height:40px;margin-top:22px}

/* Results */
.results{position:absolute;left:0;top:1807px;width:1200px;height:1049px;background:#fff}
.results .label{position:absolute;top:84px;left:0;width:1200px;text-align:center}
.results h2{position:absolute;top:108px;left:0;width:1200px;text-align:center;font-size:20px}
.result-text{position:absolute;width:300px}
.result-text h3{font-size:16px;font-weight:700;color:var(--navy)}
.result-text h4{font-size:13px;font-weight:600;color:var(--navy);margin-top:18px;line-height:19px}
.result-text p{font-size:12px;line-height:20px;margin-top:12px}
.chart{position:absolute;background:#fff;border:1px solid var(--line);box-shadow:0 8px 24px rgba(0,0,0,.1)}
.chart text{font-family:Arial,sans-serif}
.chart .tab{font-size:9px;fill:var(--chart-line)}
.chart .axis{font-size:8px;fill:#777}
.chart .small{font-size:8px;fill:#555}
.pointer{position:absolute}

/* Info request */
.info{position:absolute;left:0;top:2856px;width:1200px;height:344px;background:linear-gradient(180deg,#1a78dc,#46aef5);overflow:hidden;text-align:center;color:#fff}
.info h2{position:absolute;top:84px;left:0;width:1200px;font-size:28px;font-weight:600}
.info p{position:absolute;top:136px;left:210px;width:780px;font-size:15px;line-height:25px}
.info .btn{position:absolute;left:480px;top:217px;width:240px;height:44px;background:#fff;color:var(--blue);text-transform:none;font-size:14px;letter-spacing:0;box-shadow:none}

/* Testimonials */
.testimonials{position:absolute;left:0;top:3200px;width:1200px;height:387px;background:#fff}
.testimonials .label{position:absolute;top:78px;left:0;width:1200px;text-align:center}
.testimonials h2{position:absolute;top:102px;left:0;width:1200px;text-align:center;font-size:20px}
.quote{position:absolute;top:158px;width:280px;height:224px;background:var(--bg-soft);border:1px solid var(--line);padding:22px 18px}
.quote .who{display:flex;gap:12px;align-items:center}
.avatar{width:42px;height:42px;border-radius:50%;background:linear-gradient(135deg,#c9a58a,#6e5a4e)}
.quote .name{font-family:"Montserrat",Arial,sans-serif;font-size:13px;font-weight:600;color:var(--navy)}
.quote .role{font-size:11px;color:var(--blue);margin-top:2px}
.quote p{font-size:11px;line-height:17px;font-style:italic;margin-top:14px}

/* Newsletter */
.newsletter{position:absolute;left:0;top:3587px;width:1200px;height:441px;background:linear-gradient(180deg,#1a73d8,#4ab3f7);overflow:hidden;text-align:center;color:#fff}
.newsletter h2{position:absolute;top:234px;left:0;width:1200px;font-size:19px;font-weight:700}
.newsletter p{position:absolute;top:272px;left:0;width:1200px;font-size:13px}
.subscribe{position:absolute;left:364px;top:310px;width:475px;height:50px;background:#fff;border-radius:3px;display:flex}
.subscribe span{flex:1;text-align:left;font-size:12px;color:var(--muted);padding:17px 16px}
.subscribe b{width:140px;background:var(--blue);border-radius:0 3px 3px 0;font-family:"Montserrat",Arial,sans-serif;font-size:15px;line-height:50px;font-weight:600;color:#fff}

/* Footer */
.footer{position:absolute;left:0;top:4028px;width:1200px;height:110px;background:#fff}
.footer .brand{position:absolute;left:157px;top:38px;color:var(--blue)}
.footer small{position:absolute;top:50px;font-size:11px;color:var(--blue)}
</style>
</head>
<body>

<header class="hero">
  <svg class="hero-wave" viewBox="0 0 1200 720" aria-hidden="true">
    <polyline points="0,420 120,400 260,430 420,380 560,410 700,330 860,360 980,250 1100,290 1200,230" fill="none" stroke="rgba(255,255,255,.18)" stroke-width="2"/>
    <circle cx="980" cy="250" r="5" fill="rgba(255,255,255,.3)"/>
    <circle cx="700" cy="330" r="5" fill="rgba(255,255,255,.3)"/>
    <path d="M0,560 C300,520 700,520 1200,500 L1200,720 L0,720 Z" fill="#ffffff"/>
    <path d="M0,520 C400,500 800,480 1200,440 L1200,500 C700,520 300,520 0,560 Z" fill="rgba(255,255,255,.25)"/>
  </svg>
  <nav class="nav">
    <div class="brand">BRIVOLTA<i></i></div>
    <a style="left:505px">About</a>
    <a style="left:590px">Pricing</a>
    <a style="left:668px">Contact</a>
    <a style="left:922px">Result</a>
    <a style="left:1005px">References</a>
  </nav>
  <h1>French Backlinks on Quality<br>Magazines and Blogs</h1>
  <div class="sub">Trust Flow Target 15-20<br>Only quality backlinks help increase your traffic on <b>Quendo</b></div>
  <form class="form-card">
    <h2>Information and Rates</h2>
    <div class="hint">We'll give you straight answers!</div>
    <div class="rule"></div>
    <div class="row"><div class="field">Your Name *</div><div class="field">Your Email *</div></div>
    <div class="field wide">Website URL *</div>
    <div class="field area">How can we help you?</div>
    <span class="btn">Submit your information <svg width="14" height="10" viewBox="0 0 14 10"><path d="M0 5h12M8 1l4 4-4 4" stroke="#fff" stroke-width="1.6" fill="none"/></svg></span>
  </form>
</header>

<div class="logos">
  <span>ornvale</span><span>Pellquist</span><span>Trendarro</span><span>sabrelock</span><span>QUILLMARK</span>
</div>

<section class="about">
  <div class="label">Brivolta</div>
  <h2 class="section-title">About Brivolta</h2>
  <p>Brivolta is a netlinking service. Netlinking is about getting hyperlinks to a website from other websites in order to improve the reputation of the site in search engines such as Quendo. Netlinking is reputed to be the most important site ranking factor in modern search engines. Our clients are European SMEs with SEO knowledge and who want help with their netlinking.</p>
  <span class="btn">Read more <svg width="14" height="10" viewBox="0 0 14 10"><path d="M0 5h12M8 1l4 4-4 4" stroke="#fff" stroke-width="1.6" fill="none"/></svg></span>
</section>

<section class="steps">
  <div class="step s1"><span class="tag">Step 1</span>
    <svg width="34" height="34" viewBox="0 0 34 34"><circle cx="17" cy="11" r="6" fill="none" stroke="#fff" stroke-width="2"/><path d="M6 31c2-8 20-8 22 0" fill="none" stroke="#fff" stroke-width="2"/></svg>
    <h3>Identify a good Opportunity</h3></div>
  <div class="step s2"><span class="tag">Step 2</span>
    <svg width="34" height="34" viewBox="0 0 34 34"><circle cx="17" cy="17" r="6" fill="none" stroke="#fff" stroke-width="2"/><circle cx="17" cy="17" r="12" fill="none" stroke="#fff" stroke-width="2" stroke-dasharray="5 4"/></svg>
    <h3>Optimize Your Page</h3></div>
  <div class="step s3"><span class="tag">Step 3</span>
    <svg width="34" height="34" viewBox="0 0 34 34"><rect x="4" y="13" width="15" height="8" rx="4" fill="none" stroke="#fff" stroke-width="2" transform="rotate(-45 11 17)"/><rect x="15" y="13" width="15" height="8" rx="4" fill="none" stroke="#fff" stroke-width="2" transform="rotate(-45 22 17)"/></svg>
    <h3>Get links: the Netlinking</h3></div>
  <div class="step s4"><span class="tag">Step 4</span>
    <svg width="34" height="34" viewBox="0 0 34 34"><rect x="4" y="6" width="26" height="10" fill="none" stroke="#fff" stroke-width="2"/><path d="M10 16v12M24 16v12M8 28h18" stroke="#fff" stroke-width="2"/></svg>
    <h3>Measure the Results</h3></div>
  <div class="steps-copy">
    <div class="label">Brivolta</div>
    <h2>4 steps to improve your natural SEO on Quendo</h2>
    <p>Have you ever wondered why some sites appear before others on Quendo? How does Quendo determine the placement of a site in its search results?</p>
    <span class="btn">Learn more <svg width="14" height="10" viewBox="0 0 14 10"><path d="M0 5h12M8 1l4 4-4 4" stroke="#fff" stroke-width="1.6" fill="none"/></svg></span>
  </div>
</section>

<section class="results">
  <div class="label">Brivolta</div>
  <h2 class="section-title">Examples of results obtained with our backlinks</h2>

  <div class="result-text" style="left:160px;top:207px">
    <h3>From 0 to 26 000 visits / month</h3>
    <h4>And it continues to increase!</h4>
    <p>Lorem ipsum dolor sit amet, consectetur adipiscing elit, sed do eiusmod tempor incididunt ut labore dolore.</p>
  </div>
  <svg class="pointer" style="left:488px;top:246px" width="46" height="60" viewBox="0 0 46 60"><path d="M46 0 L0 30 L46 60 Z" fill="var(--pointer)"/></svg>
  <svg class="chart" style="left:532px;top:155px" width="508" height="278" viewBox="0 0 508 278">
    <rect width="508" height="20" fill="#f4f5f6"/><text x="10" y="14" font-size="9" fill="#333">Explorer</text>
    <text class="tab" x="10" y="38">Summary</text><text class="tab" x="62" y="38">Site Usage</text><text class="tab" x="122" y="38">Ecommerce</text><text class="tab" x="186" y="38">Revenue</text>
    <rect x="10" y="52" width="50" height="14" fill="#fff" stroke="#ccc"/><text class="small" x="14" y="62">Sessions</text>
    <rect x="370" y="52" width="76" height="14" fill="#eee" stroke="#ccc"/><text class="small" x="375" y="62">Day</text><text class="small" x="395" y="62">Week</text><text class="small" x="420" y="62">Month</text>
    <circle cx="16" cy="82" r="3" fill="var(--chart-line)"/><text x="24" y="85" font-size="8" fill="#333">Sessions</text>
    <line x1="10" y1="118" x2="498" y2="118" stroke="#eee"/><line x1="10" y1="178" x2="498" y2="178" stroke="#eee"/>
    <path d="M10,236 L60,233 L110,230 L160,222 L200,210 L240,172 L280,182 L330,186 L370,190 L410,192 L440,184 L470,170 L498,140 L498,250 L10,250 Z" fill="var(--chart-fill)"/>
    <polyline points="10,236 60,233 110,230 160,222 200,210 240,172 280,182 330,186 370,190 410,192 440,184 470,170 498,140" fill="none" stroke="var(--chart-line)" stroke-width="2.5"/>
    <text class="axis" x="20" y="266">April 2017</text><text class="axis" x="130" y="266">July 2017</text><text class="axis" x="230" y="266">October 2017</text><text class="axis" x="340" y="266">January 2018</text><text class="axis" x="440" y="266">July 2018</text>
  </svg>

  <svg class="chart" style="left:160px;top:442px" width="505" height="242" viewBox="0 0 505 242">
    <rect width="505" height="20" fill="#f4f5f6"/><text x="10" y="14" font-size="9" fill="#333">Explorer</text>
    <text class="tab" x="10" y="38">Summary</text><text class="tab" x="62" y="38">Site Usage</text><text class="tab" x="122" y="38">Goal Set 1</text><text class="tab" x="180" y="38">Goal Set 2</text><text class="tab" x="238" y="38">Ecommerce</text>
    <rect x="10" y="52" width="50" height="14" fill="#fff" stroke="#ccc"/><text class="small" x="14" y="62">Sessions</text>
    <rect x="370" y="52" width="76" height="14" fill="#eee" stroke="#ccc"/><text class="small" x="375" y="62">Day</text><text class="small" x="395" y="62">Week</text><text class="small" x="420" y="62">Month</text>
    <line x1="10" y1="120" x2="495" y2="120" stroke="#eee"/><line x1="10" y1="170" x2="495" y2="170" stroke="#eee"/>
    <path d="M10,190 L60,188 L110,184 L150,170 L190,162 L230,158 L270,160 L310,158 L350,154 L390,146 L420,150 L460,138 L495,128 L495,210 L10,210 Z" fill="var(--chart-fill)"/>
    <polyline points="10,190 60,188 110,184 150,170 190,162 230,158 270,160 310,158 350,154 390,146 420,150 460,138 495,128" fill="none" stroke="var(--chart-line)" stroke-width="2.5"/>
    <text class="axis" x="70" y="228">July 2017</text><text class="axis" x="200" y="228">October 2017</text><text class="axis" x="320" y="228">January 2018</text><text class="axis" x="430" y="228">April 2018</text>
  </svg>
  <svg class="pointer" style="left:665px;top:533px" width="46" height="60" viewBox="0 0 46 60"><path d="M0 0 L46 30 L0 60 Z" fill="var(--pointer)"/></svg>
  <div class="result-text" style="left:739px;top:491px">
    <h3>From 1,200 to 4,400 visits / month</h3>
    <h4>Traffic from Quendo has more than tripled in 12 months.</h4>
    <p>Lorem ipsum dolor sit amet, consectetur adipiscing elit, sed do eiusmod tempor incididunt ut labore dolore.</p>
  </div>

  <div class="result-text" style="left:160px;top:781px">
    <h3>From 0 to 60 000 visits / week</h3>
    <h4>This is more than 240 000 visits per month for this site.</h4>
    <p>Lorem ipsum dolor sit amet, consectetur adipiscing elit, sed do eiusmod tempor incididunt ut labore dolore.</p>
  </div>
  <svg class="pointer" style="left:488px;top:822px" width="46" height="60" viewBox="0 0 46 60"><path d="M46 0 L0 30 L46 60 Z" fill="var(--pointer)"/></svg>
  <svg class="chart" style="left:532px;top:726px" width="508" height="240" viewBox="0 0 508 240">
    <rect width="508" height="20" fill="#f4f5f6"/><text x="10" y="14" font-size="9" fill="#333">Explorer</text>
    <text class="tab" x="10" y="38">Summary</text><text class="tab" x="62" y="38">Site Usage</text><text class="tab" x="122" y="38">Ecommerce</text><text class="tab" x="186" y="38">Revenue</text>
    <rect x="10" y="52" width="50" height="14" fill="#fff" stroke="#ccc"/><text class="small" x="14" y="62">Sessions</text>
    <rect x="370" y="52" width="76" height="14" fill="#eee" stroke="#ccc"/><text class="small" x="375" y="62">Day</text><text class="small" x="395" y="62">Week</text><text class="small" x="420" y="62">Month</text>
    <circle cx="16" cy="80" r="3" fill="var(--chart-line)"/><text x="24" y="83" font-size="8" fill="#333">Sessions</text>
    <line x1="10" y1="150" x2="498" y2="150" stroke="#eee"/>
    <path d="M10,212 L80,212 L120,210 L140,200 L160,206 L180,190 L200,182 L220,170 L240,175 L260,160 L280,166 L300,150 L320,160 L340,146 L360,152 L380,140 L400,150 L420,136 L440,146 L460,138 L480,142 L498,134 L498,212 Z" fill="var(--chart-fill)"/>
    <polyline points="10,212 80,212 120,210 140,200 160,206 180,190 200,182 220,170 240,175 260,160 280,166 300,150 320,160 340,146 360,152 380,140 400,150 420,136 440,146 460,138 480,142 498,134" fill="none" stroke="var(--chart-line)" stroke-width="2"/>
    <text class="axis" x="40" y="228">July 2017</text><text class="axis" x="150" y="228">October 2017</text><text class="axis" x="260" y="228">January 2018</text><text class="axis" x="370" y="228">April 2018</text><text class="axis" x="450" y="228">July 2018</text>
  </svg>
</section>

<section class="info">
  <svg class="abs" style="left:0;top:0" width="1200" height="344" viewBox="0 0 1200 344" aria-hidden="true">
    <circle cx="320" cy="90" r="30" fill="rgba(255,255,255,.14)"/>
    <circle cx="275" cy="120" r="14" fill="rgba(255,255,255,.12)"/>
    <circle cx="1110" cy="192" r="28" fill="rgba(255,255,255,.2)"/>
    <circle cx="930" cy="250" r="10" fill="rgba(255,255,255,.15)"/>
    <circle cx="140" cy="300" r="40" fill="rgba(255,255,255,.1)"/>
  </svg>
  <h2>Information request</h2>
  <p>Would you like more information or pricing? Fill in the short contact form and tell us about your SEO needs and goals. The rates of the backlinks vary according to the theme.</p>
  <span class="btn">View Our Pricing Plan <svg width="14" height="10" viewBox="0 0 14 10"><path d="M0 5h12M8 1l4 4-4 4" stroke="#1e7fe0" stroke-width="1.6" fill="none"/></svg></span>
</section>

<section class="testimonials">
  <div class="label">Brivolta</div>
  <h2 class="section-title">Users Testimonials</h2>
  <article class="quote" style="left:160px">
    <div class="who"><div class="avatar" role="img" aria-label="Portrait photo of Lucien Maréchal"></div><div><div class="name">Lucien Maréchal</div><div class="role">Owner · Velora Gems</div></div></div>
    <p>They drove netlinking campaigns for our online store, which resulted in more than 50 quality links and improved the overall positioning of the site on Quendo.</p>
  </article>
  <article class="quote" style="left:460px">
    <div class="who"><div class="avatar" role="img" aria-label="Portrait photo of Paul Devaux"></div><div><div class="name">Paul Devaux</div><div class="role">Owner · Ambra Voyages</div></div></div>
    <p>Thanks to their work, the important pages of my site are now visible in Quendo's first search results for competitive and important keywords for my travel agency. They are accessible and answer all my questions quickly.</p>
  </article>
  <article class="quote" style="left:760px">
    <div class="who"><div class="avatar" role="img" aria-label="Portrait photo of Henri Castel"></div><div><div class="name">Henri Castel</div><div class="role">Owner · Castel Media</div></div></div>
    <p>In a few months, we have moved to the first page of Quendo for all targeted keywords. The agency is very professional and works methodically. The reports they give us each month are easy to understand and help track the progress of the project.</p>
  </article>
</section>

<section class="newsletter">
  <svg class="abs" style="left:0;top:0" width="1200" height="441" viewBox="0 0 1200 441" aria-hidden="true">
    <path d="M0,0 L1200,0 L1200,30 L600,170 L0,30 Z" fill="#ffffff"/>
    <path d="M0,30 L600,170 L1200,30 L1200,60 L600,190 L0,60 Z" fill="rgba(255,255,255,.12)"/>
  </svg>
  <h2>Brivolta getting all the updates?</h2>
  <p>Get all the updates, changes and news in your e-mail box</p>
  <div class="subscribe"><span>Enter your email address...</span><b>Submit</b></div>
</section>

<footer class="footer">
  <div class="brand">BRIVOLTA<i></i></div>
  <small style="left:483px">© 2019 BRIVOLTA - All Rights Reserved</small>
  <small style="left:822px">Privacy Policy</small>
  <small style="left:930px">Terms &amp; Condition</small>
</footer>

</body>
</html>
```